Professional Business Cards

We need a nice looking, profession and modern business card for our new company. Our logo is attatched

Target Market(s)

Young Professionals

Industry/Entity Type

Financial

Contact Information for Business Card

FRONT

Morvane Tally Pty Ltd
Level 22, Halden Court, 48 Wirrapool St
Sydney NSW 2000
ABN : 57 304 918 226

Derek Wallis - Chief Operations Officer
P : 02 7153 2819
M: 0418 395 207
derek@morvanetally,com

BACK

- Cryptocurrency Exchange Services
- Cryptocurrency Mining Operations
- Cryptocurrency Investment Fund Offering

Font styles to use
Sans Serif

Colors
0255a3
9d9d9d

```html
<!DOCTYPE html>
<html lang="en">
<head>
<meta charset="utf-8">
<title>Morvane Tally Business Cards</title>
<link href="https://fonts.googleapis.com/css2?family=Questrial&display=swap" rel="stylesheet">
<style>
  :root {
    --brand-blue: #0255a3;
    --brand-grey: #9d9d9d;
    --dark-grey: #5f6062;
    --text-grey: #6b6b6b;
    --card-white: #f4f4f4;
    --faint-grey: #e2e2e4;
    --faint-blue: #dde1ee;
    --backdrop: #2a2a2a;
  }
  * { margin: 0; padding: 0; box-sizing: border-box; }
  html, body {
    width: 1200px; height: 834px; overflow: hidden;
    background: var(--backdrop);
    font-family: "Questrial", sans-serif;
  }
  .stage {
    position: relative; width: 1200px; height: 834px;
    display: flex; align-items: center; justify-content: center; gap: 40px;
  }
  .card {
    position: relative; width: 540px; height: 309px;
    background: var(--card-white); overflow: hidden;
    box-shadow: 0 12px 30px rgba(0,0,0,.45);
  }
  .card-art { position: absolute; inset: 0; }
  .wordmark {
    position: absolute; display: flex; align-items: center; gap: 10px;
    color: var(--brand-blue); font-size: 30px; letter-spacing: 1px;
    text-transform: uppercase; white-space: nowrap;
  }
  .wordmark-square {
    width: 30px; height: 30px; background: var(--brand-blue); flex: none;
  }
  .front .wordmark { left: 60px; top: 112px; }
  .services {
    position: absolute; left: 60px; top: 172px;
    color: var(--text-grey); font-size: 12px; line-height: 1.6;
  }
  .services .divider { margin: 0 6px; }
  .back .wordmark { left: 132px; top: 124px; font-size: 19px; letter-spacing: 0.5px; gap: 8px; }
  .back .wordmark-square { width: 24px; height: 24px; }
  .contact {
    position: absolute; left: 362px; top: 46px;
    color: var(--text-grey); font-size: 11px; line-height: 1.55;
  }
  .contact .person-name { color: var(--dark-grey); font-size: 19px; line-height: 1.1; }
  .contact .person-role { color: var(--brand-blue); font-size: 11px; margin-bottom: 10px; }
  .contact .company { color: var(--brand-blue); font-size: 13px; font-weight: 700; }
  .contact .channels { margin-top: 10px; list-style: none; }
  .contact .channels li { display: flex; align-items: center; gap: 8px; }
  .contact .channels svg { width: 12px; height: 12px; flex: none; }
</style>
</head>
<body>
<main class="stage">

  <section class="card front">
    <svg class="card-art" viewBox="0 0 540 309" aria-hidden="true">
      <polygon points="400,0 540,0 540,250" fill="var(--brand-blue)"/>
      <polygon points="445,0 540,0 540,185" fill="var(--card-white)"/>
      <polygon points="462,0 540,0 540,160" fill="var(--dark-grey)"/>
      <polygon points="505,0 540,0 540,75" fill="var(--card-white)"/>
    </svg>
    <div class="wordmark"><span class="wordmark-square"></span>Morvane Tally</div>
    <p class="services">
      Cryptocurrency Exchange Services<span class="divider">|</span>Cryptocurrency Mining Operations<br>
      Cryptocurrency Investment Fund Offering
    </p>
  </section>

  <section class="card back">
    <svg class="card-art" viewBox="0 0 540 309" aria-hidden="true">
      <rect x="0" y="0" width="14" height="309" fill="var(--faint-blue)"/>
      <rect x="30" y="20" width="90" height="100" fill="var(--faint-grey)"/>
      <rect x="30" y="160" width="90" height="100" fill="var(--faint-grey)"/>
      <rect x="0" y="280" width="60" height="29" fill="var(--faint-blue)"/>
    </svg>
    <div class="wordmark"><span class="wordmark-square"></span>Morvane Tally</div>
    <div class="contact">
      <p class="person-name">Derek Wallis</p>
      <p class="person-role">Chief Operations Officer</p>
      <p class="company">Morvane Tally Pty Ltd</p>
      <p>Level 22, Halden Court<br>48 Wirrapool St<br>Sydney NSW 2000<br>ABN : 57 304 918 226</p>
      <ul class="channels">
        <li>
          <svg viewBox="0 0 12 12"><path d="M2.5 1 L4.5 1 L5.2 3.5 L4 4.5 Q5 6.8 7.5 8 L8.5 6.8 L11 7.5 L11 9.5 Q10.5 11 9 11 Q1 10 1 2.5 Q1 1 2.5 1Z" fill="none" stroke="var(--brand-blue)" stroke-width="1"/></svg>
          02 7153 2819
        </li>
        <li>
          <svg viewBox="0 0 12 12"><rect x="3" y="0.5" width="6" height="11" rx="1" fill="none" stroke="var(--brand-blue)" stroke-width="1"/><line x1="5" y1="9.5" x2="7" y2="9.5" stroke="var(--brand-blue)"/></svg>
          0418 395 207
        </li>
        <li>
          <svg viewBox="0 0 12 12"><rect x="0.5" y="2" width="11" height="8" fill="none" stroke="var(--brand-blue)" stroke-width="1"/><polyline points="0.5,2 6,6.5 11.5,2" fill="none" stroke="var(--brand-blue)" stroke-width="1"/></svg>
          derek@morvanetally.com
        </li>
      </ul>
    </div>
  </section>

</main>
</body>
</html>
```